Business Card Design Project

parking lot sealing and striping company

Industry/Entity Type

Business

Contact Information for Business Card

See pics below, blue and gray colors

```html
<!DOCTYPE html>
<html lang="en">
<head>
<meta charset="utf-8">
<title>Keystone Paving – Business Card</title>
<link rel="stylesheet" href="https://fonts.googleapis.com/css2?family=Open+Sans:wght@400;600;700&display=swap">
<style>
  :root {
    --page-bg: #ffffff;
    --card-dark: #111112;
    --card-mid: #1d1d1f;
    --silver: #d4d4d6;
    --silver-dark: #8e8e92;
    --text-light: #c9c9cc;
    --blue: #2c3fae;
    --figure-tone: #b9b9bd;
  }
  * { margin: 0; padding: 0; box-sizing: border-box; }
  html, body { width: 1200px; height: 900px; overflow: hidden; background: var(--page-bg); }
  body { position: relative; font-family: "Open Sans", Arial, sans-serif; }

  .card {
    position: absolute; left: 100px; top: 170px;
    width: 1000px; height: 560px; border-radius: 40px; overflow: hidden;
    background: radial-gradient(ellipse at 50% 30%, var(--card-mid), var(--card-dark) 75%);
  }

  .brand {
    position: absolute; left: 56px; top: 88px;
    display: flex; align-items: center; gap: 18px;
  }
  .brand-dot { width: 26px; height: 26px; border-radius: 50%; background: var(--blue); }
  .brand-name {
    font-size: 66px; font-weight: 700; color: var(--silver); letter-spacing: 1px; line-height: 1;
  }
  .brand-tagline {
    position: absolute; left: 100px; top: 172px;
    font-size: 26px; font-weight: 700; letter-spacing: 8px; color: var(--silver);
  }

  .figure-area {
    position: absolute; left: 770px; top: 40px; width: 200px; height: 200px; border-radius: 8px;
    background: linear-gradient(180deg, var(--figure-tone), var(--silver-dark) 70%, transparent);
    opacity: .55;
  }

  .divider {
    position: absolute; left: 0; right: 0; top: 296px; height: 7px;
    background: linear-gradient(90deg, var(--silver-dark), var(--silver), var(--silver-dark));
  }

  .contact { position: absolute; left: 50px; top: 352px; }
  .contact-row { display: flex; align-items: center; gap: 16px; color: var(--text-light); font-weight: 600; }
  .contact-row svg { flex: none; }
  .contact-phone { font-size: 38px; font-weight: 700; margin-bottom: 34px; }
  .contact-line { font-size: 25px; margin-bottom: 20px; }

  .services {
    position: absolute; top: 318px; list-style: none;
    color: var(--text-light); font-size: 18px; text-transform: uppercase;
  }
  .services li { position: relative; padding-left: 22px; height: 37px; line-height: 37px; }
  .services li::before {
    content: ""; position: absolute; left: 0; top: 15px;
    width: 7px; height: 7px; border-radius: 50%; background: var(--blue);
  }
  .services-primary { left: 420px; }
  .services-secondary { left: 655px; top: 310px; }
</style>
</head>
<body>
  <div class="card">
    <div class="brand">
      <span class="brand-dot"></span>
      <span class="brand-name">Keystone Paving</span>
    </div>
    <div class="brand-tagline">SEALING AND STRIPING</div>

    <div class="figure-area" role="img" aria-label="Silhouette illustration of a worker pushing a line striping machine"></div>

    <div class="divider"></div>

    <div class="contact">
      <div class="contact-row contact-phone">
        <svg width="32" height="34" viewBox="0 0 24 24"><path fill="#2c3fae" d="M6.6 10.8a15.1 15.1 0 0 0 6.6 6.6l2.2-2.2c.3-.3.7-.4 1-.2 1.1.4 2.3.6 3.6.6.6 0 1 .4 1 1V20c0 .6-.4 1-1 1A17 17 0 0 1 3 4c0-.6.4-1 1-1h3.5c.6 0 1 .4 1 1 0 1.3.2 2.5.6 3.6.1.3 0 .7-.2 1z"/></svg>
        <span>5550 123 456</span>
      </div>
      <div class="contact-row contact-line">
        <svg width="32" height="32" viewBox="0 0 24 24" fill="none" stroke="#2c3fae" stroke-width="2"><circle cx="12" cy="12" r="10"/><path d="M2 12h20M12 2c3 3 3 17 0 20M12 2c-3 3-3 17 0 20M4 7h16M4 17h16"/></svg>
        <span>www.keystonepv.com</span>
      </div>
      <div class="contact-row contact-line">
        <svg width="32" height="28" viewBox="0 0 24 20"><rect x="1" y="2" width="22" height="16" rx="2" fill="#2c3fae"/><path d="M2 3l10 8 10-8" fill="none" stroke="#111112" stroke-width="1.6"/></svg>
        <span>info@keystonepv.com</span>
      </div>
    </div>

    <ul class="services services-primary">
      <li>Asphalt Sealocating</li>
      <li>Parking Lot Striping</li>
      <li>Curbpainting</li>
      <li>Crack Filling</li>
      <li>Speedbrakers</li>
      <li>Cincrete Rapair</li>
    </ul>
    <ul class="services services-secondary">
      <li>Concreteinstallation</li>
      <li>Drainage Repairs</li>
      <li>ADA Compliance</li>
      <li>Handicap Signs</li>
      <li>Asphalt Repair / Patch</li>
      <li>Asphalt Pavings</li>
    </ul>
  </div>
</body>
</html>
```